Make a CV more classy for an orthopaedic hand surgeon

I actually don't want a resume with many pictures etc. I want a CV that is classy, and would be attractive to lawyers. I want you to keep the same content in my current CV just rearrange things if necessary and make it nice, with nice headers and organization. Again, like the sleek, classy, luxury, but professional look. I want lawyers and other recruiters to look at my CV and know I am high class

Target Market(s)

Lawyers, Consulting gigs--they want to see that I am smart and have a lot of accolades

Industry/Entity Type

Medicine

Colors
0054AA
0677BA
7BADD7
CADEEF
E8F1F8

Requirements
Must have
• Classy, luxury, professional
Nice to have
• NA
Should not have
• Additional photos, resume-type look--bubbles everywhere, boxes circled. Should look like the format it is in already, just spiced up and organized better with nice fancy headers and sleek look

```html
<!DOCTYPE html>
<html lang="en">
<head>
<meta charset="utf-8">
<title>Adaeze Morrow, M.D — Curriculum Vitae</title>
<link href="https://fonts.googleapis.com/css2?family=Montserrat:wght@500;800&family=Open+Sans:wght@400;500&display=swap" rel="stylesheet">
<style>
  :root{
    --canvas:#f1f2f4;
    --paper:#ffffff;
    --ink:#0b1a3f;
    --heading:#1c2542;
    --body:#2b3042;
    --navy:#0d3c8c;
    --royal:#2a62b2;
    --accent:#4a8fdc;
    --ice:#e8f1f8;
    --mist:#cadeef;
    --sky:#c4dbf7;
    --photo-a:#d9d5d2;
    --photo-b:#3a2a24;
  }
  *{box-sizing:border-box;margin:0;padding:0}
  html,body{width:1200px;height:840px;overflow:hidden}
  body{background:var(--canvas);font-family:"Open Sans",Arial,sans-serif;color:var(--body);position:relative}
  .cv{position:absolute;left:316px;top:20px;width:567px;height:800px;background:var(--paper);
      box-shadow:0 6px 24px rgba(20,30,60,.14);overflow:hidden}
  .cv-shapes{position:absolute;inset:0}
  .portrait{position:absolute;left:33px;top:44px;width:186px;height:260px;
      background:linear-gradient(180deg,var(--photo-a) 0%,#b9a79c 45%,var(--photo-b) 100%)}
  .abs{position:absolute;white-space:nowrap}
  .name{left:255px;top:44px;font-family:"Montserrat",Arial,sans-serif;font-weight:800;font-size:34px;
      line-height:40px;letter-spacing:6px;color:var(--ink)}
  .credential{left:255px;top:134px;width:250px;height:29px;background:var(--navy);color:#fff;
      font-family:"Montserrat",Arial,sans-serif;font-weight:500;font-size:10.5px;line-height:29px;padding-left:16px;
      clip-path:polygon(0 0,100% 0,100% 55%,94% 100%,0 100%)}
  .socials{left:255px;top:183px;display:flex;gap:22px;font-size:9.5px;color:var(--ink)}
  .social{display:flex;align-items:center;gap:6px}
  .social-dot{width:8px;height:8px;border-radius:2px;background:var(--accent)}
  .profile-band{position:absolute;left:229px;top:217px;width:317px;height:123px;background:var(--ice)}
  .section-title{font-family:"Open Sans",Arial,sans-serif;font-weight:500;font-size:12px;letter-spacing:3px;color:var(--heading)}
  .rule{position:absolute;height:1px;background:var(--heading)}
  .text{font-size:7.4px;line-height:12px;color:var(--body);white-space:normal}
  .org{font-size:7.6px;font-weight:500;color:var(--ink)}
  .meta{font-size:6.8px;color:var(--accent)}
  .sidebar-title{font-size:11.5px;letter-spacing:3px;color:#fff;font-weight:500}
  .side-item{font-size:8.8px;line-height:12px;color:#fff;letter-spacing:.3px}
  .skill{font-size:8.8px;color:#fff}
</style>
</head>
<body>
<main class="cv">
  <svg class="cv-shapes" width="567" height="800" viewBox="0 0 567 800" aria-hidden="true">
    <defs>
      <linearGradient id="edge" x1="0" y1="0" x2="0" y2="1">
        <stop offset="0" stop-color="#d8e7fa"/><stop offset="1" stop-color="#ffffff"/>
      </linearGradient>
      <linearGradient id="side" x1="0" y1="0" x2="0" y2="1">
        <stop offset="0" stop-color="#0d3c8c"/><stop offset="1" stop-color="#2a62b2"/>
      </linearGradient>
    </defs>
    <polygon points="0,0 77,0 121,44 33,44 33,800 0,800" fill="url(#edge)"/>
    <rect x="546" y="0" width="21" height="800" fill="#c4dbf7"/>
    <polygon points="23,285 77,251 229,311 229,800 23,800" fill="url(#side)"/>
    <polygon points="509,800 567,743 567,800" fill="#0b1a3f"/>
  </svg>

  <div class="portrait" role="img" aria-label="Professional portrait photograph of the surgeon"></div>

  <h1 class="abs name">Adaeze<br>Morrow, M.D</h1>
  <div class="abs credential">Board Certified, Hand Subspecialty Certified</div>
  <div class="abs socials">
    <span class="social"><span class="social-dot"></span>@drmorrow</span>
    <span class="social"><span class="social-dot"></span>Adaeze Morrow</span>
    <span class="social"><span class="social-dot"></span>@drmorrow</span>
  </div>

  <!-- sidebar -->
  <h2 class="abs sidebar-title" style="left:45px;top:343px">PERSONAL INFO</h2>
  <div class="abs side-item" style="left:45px;top:380px">Phone<br>+64 55501 4271</div>
  <div class="abs side-item" style="left:45px;top:411px">Email<br>office@morrowhand.com</div>
  <div class="abs side-item" style="left:45px;top:443px">Website<br>www.morrowhand.com</div>
  <div class="abs side-item" style="left:45px;top:476px">Linkedin<br>linkedin.com/adaezemorrow</div>
  <div class="abs side-item" style="left:45px;top:508px">Address<br>18 Harbour Lane, Westvale 645</div>
  <h2 class="abs sidebar-title" style="left:45px;top:559px">SKILLS</h2>
  <div class="abs skill" style="left:45px;top:600px">Skill One</div>
  <div class="abs skill" style="left:45px;top:629px">Skill Two</div>
  <div class="abs skill" style="left:45px;top:658px">Skill Three</div>
  <div class="abs skill" style="left:45px;top:687px">Skill Four</div>
  <div class="abs skill" style="left:45px;top:716px">Skill Five</div>
  <div class="abs skill" style="left:45px;top:745px">Skill Six</div>

  <!-- profile -->
  <div class="profile-band"></div>
  <h2 class="abs section-title" style="left:255px;top:233px">PROFILE</h2>
  <div class="rule" style="left:336px;top:242px;width:181px"></div>
  <p class="abs text" style="left:255px;top:254px;width:264px">Enim diam vulputate ut pharetra sit. Amet cursus sit amet dictum sit amet. Ultrices dui sapien eget mi proin sed libero enim. Duis convallis convallis tellus id interdum velit laoreet id donec. Ac tortor vitae purus faucibus. Nunc eget lorem dolor sed. Eget mauris pharetra et ultrices neque ornare aenean. Sit amet volutpat consequat mauris nunc congue nisi vitae</p>

  <!-- experience -->
  <h2 class="abs section-title" style="left:255px;top:361px">EXPERIENCE</h2>
  <div class="rule" style="left:362px;top:370px;width:155px"></div>
  <div class="abs org" style="left:255px;top:388px">COMPANY NAME</div>
  <div class="abs meta" style="left:255px;top:402px">Job Title</div>
  <div class="abs meta" style="left:476px;top:402px">2014 - 2015</div>
  <p class="abs text" style="left:255px;top:414px;width:264px">Nulla posuere sollicitudin aliquam ultrices sagittis. Est velit egestas duini id ornare arcu odio. Amet consectetur adipiscing elit ut aliquam.</p>
  <div class="abs org" style="left:255px;top:453px">COMPANY NAME</div>
  <div class="abs meta" style="left:255px;top:467px">Job Title</div>
  <div class="abs meta" style="left:476px;top:467px">2014 - 2015</div>
  <p class="abs text" style="left:255px;top:479px;width:264px">Nulla posuere sollicitudin aliquam ultrices sagittis. Est velit egestas duini id ornare arcu odio. Amet consectetur adipiscing elit ut aliquam.</p>

  <!-- education -->
  <h2 class="abs section-title" style="left:255px;top:534px">EDUCATION</h2>
  <div class="rule" style="left:362px;top:543px;width:155px"></div>
  <div class="abs org" style="left:255px;top:562px">UNIVERSITY NAME</div>
  <div class="abs org" style="left:255px;top:580px;font-size:7px">Major Subject</div>
  <div class="abs meta" style="left:259px;top:592px">2009 - 2013</div>
  <p class="abs text" style="left:328px;top:578px;width:191px">Nulla posuere sollicitudin aliquam ultrices sagittis. Est velit egestas duini id ornare arcu odio. Amet consectetur adipiscing elit ut aliquam.</p>

  <!-- achievements -->
  <h2 class="abs section-title" style="left:255px;top:648px">ACHIEVEMENTS</h2>
  <div class="rule" style="left:387px;top:657px;width:130px"></div>
  <div class="abs meta" style="left:257px;top:678px">2021</div>
  <div class="abs org" style="left:283px;top:677px">ACHIEVEMENTS</div>
  <p class="abs text" style="left:283px;top:689px;width:236px">Nulla posuere sollicitudin aliquam ultrices sagittis. Est velit egestas duini id ornare arcu odio. Amet consectetur adipiscing elit ut</p>
  <div class="abs meta" style="left:257px;top:725px">2021</div>
  <div class="abs org" style="left:283px;top:724px">ACHIEVEMENTS</div>
  <p class="abs text" style="left:283px;top:736px;width:236px">Nulla posuere sollicitudin aliquam ultrices sagittis. Est velit egestas duini id ornare arcu odio. Amet consectetur adipiscing elit ut</p>
</main>
</body>
</html>
```